Harborline Energy - needs a business card

Harborline Energy is a U.S. based diesel sourcing and distribution company that supports American oil & gas fields through providing quality product and consistent services.

Target Market(s)

Oil and Gas

Contact Information for Business Card

The background of the card must be white to ensure the logo pops.

Font styles to use
Serif
Sans Serif

Colors

Designer to choose colors to be used in the design.

Requirements
Must have
• Front of Card: Tag line: Harborline Energy, Powering America's Oil & Gas fields.
• Not sure if you guys do this part but just in case...
• Dale Menschow
• Owner/CEO
• C:555.318.4076
• E:Dmenschow@harborlineenergy.example
• W:Harborlineenergy.example
• Locations: Servicing the Powder River, DJ basin and Bakken formations.
• Back of Card: " Frac fueling is what we do. We understand how important diesel fuel is to your operation, which is why our main service line is Frac fueling. We assure our supply and stand by our service"

```html
<!DOCTYPE html>
<html lang="en">
<head>
<meta charset="utf-8">
<title>Harborline Energy – Business Card</title>
<link href="https://fonts.googleapis.com/css2?family=Lato:ital,wght@0,400;0,700;0,900;1,400&display=swap" rel="stylesheet">
<style>
  :root {
    --navy: #1f3566;
    --red: #b8262e;
    --white: #ffffff;
    --paper-bg: #e9eaec;
    --ink: #1f3566;
  }
  * { margin: 0; padding: 0; box-sizing: border-box; }
  html, body { width: 1200px; height: 900px; overflow: hidden; }
  body {
    background: var(--paper-bg);
    font-family: 'Lato', Arial, sans-serif;
    position: relative;
  }
  .card {
    position: absolute;
    left: 240px;
    width: 720px;
    height: 412px;
    background: var(--white);
    box-shadow: 0 6px 20px rgba(0,0,0,0.15);
    overflow: hidden;
  }
  .card--front { top: 28px; }
  .card--back { top: 460px; }

  /* brand lockup */
  .brand {
    display: flex;
    align-items: center;
    justify-content: center;
    gap: 12px;
  }
  .brand__dot {
    width: 30px; height: 30px;
    border-radius: 50%;
    background: var(--navy);
  }
  .brand__name {
    font-weight: 900;
    color: var(--navy);
    letter-spacing: 1px;
    text-transform: uppercase;
  }

  /* front */
  .front__top {
    height: 205px;
    display: flex;
    flex-direction: column;
    align-items: center;
    justify-content: center;
    padding-top: 6px;
  }
  .front__top .brand__name { font-size: 22px; }
  .person__name {
    margin-top: 16px;
    font-weight: 900;
    font-size: 34px;
    color: var(--red);
    text-transform: uppercase;
    letter-spacing: 0.5px;
  }
  .person__title {
    font-size: 21px;
    color: var(--navy);
    margin-top: 2px;
  }
  .info-band {
    height: 132px;
    background: var(--navy);
    display: flex;
    align-items: center;
    justify-content: center;
    color: var(--white);
    font-size: 19px;
    line-height: 1.35;
  }
  .contact { text-align: right; padding-right: 22px; }
  .divider {
    width: 2px; height: 88px;
    background: rgba(255,255,255,0.55);
  }
  .locations { padding-left: 22px; }
  .tagline-strip {
    height: 40px;
    display: flex;
    align-items: center;
    justify-content: center;
    font-weight: 700;
    font-size: 19px;
    color: var(--navy);
  }
  .red-band { height: 35px; background: var(--red); }

  /* back */
  .back__inner {
    position: absolute;
    inset: 0;
    display: flex;
    flex-direction: column;
    align-items: center;
    padding-top: 92px;
  }
  .back__inner .brand__name { font-size: 40px; letter-spacing: 3px; }
  .back__inner .brand__dot { width: 48px; height: 48px; }
  .back__rule {
    width: 600px;
    height: 2px;
    background: var(--red);
    margin-top: 36px;
  }
  .back__statement {
    margin-top: 16px;
    width: 560px;
    text-align: center;
    font-style: italic;
    font-size: 15px;
    line-height: 1.35;
    color: var(--navy);
  }
</style>
</head>
<body>
  <section class="card card--front" aria-label="Business card front">
    <div class="front__top">
      <div class="brand">
        <span class="brand__dot"></span>
        <span class="brand__name">Harborline Energy</span>
      </div>
      <h1 class="person__name">Dale Menschow</h1>
      <p class="person__title">Owner/CEO</p>
    </div>
    <div class="info-band">
      <div class="contact">
        <p>555.318.4076</p>
        <p>Dmenschow@harborlineenergy.example</p>
        <p>Harborlineenergy.example</p>
      </div>
      <span class="divider"></span>
      <div class="locations">
        <p>Servicing the Powder River</p>
        <p>DJ basin &amp;</p>
        <p>Bakken formations</p>
      </div>
    </div>
    <p class="tagline-strip">Harborline Energy, Powering America's Oil &amp; Gas fields.</p>
    <div class="red-band"></div>
  </section>

  <section class="card card--back" aria-label="Business card back">
    <div class="back__inner">
      <div class="brand">
        <span class="brand__dot"></span>
        <span class="brand__name">Harborline Energy</span>
      </div>
      <div class="back__rule"></div>
      <p class="back__statement">Frac fueling is what we do. We understand how important diesel fuel is to your operation, which is why our main service line is Frac fueling. We assure our supply and stand by our service</p>
    </div>
  </section>
</body>
</html>
```